We need a business card design for Corvana Group. We are a healthcare recruiting, wellness and education company. We partner with medical facilities to find quality candidates. We also offer free wellness courses.
The final design should communicate an emphasis on recruiting and wellness
The main purpose of the business card is to utilized it for networking events, give to hospitals, executives, VCs surgery centers and clinics. I want it to be sleek, clean, use of our brand colors and professional.

```html
<!DOCTYPE html>
<html lang="en">
<head>
<meta charset="utf-8">
<title>Corvana Group – Business Card</title>
<link href="https://fonts.googleapis.com/css2?family=Montserrat:wght@400;500;700&display=swap" rel="stylesheet">
<style>
  :root {
    --backdrop: #8c8c8a;
    --card-white: #ffffff;
    --brand-teal: #02594f;
    --brand-teal-dark: #024a42;
    --text-grey: #5a5a5a;
    --font-main: "Montserrat", Arial, sans-serif;
  }
  * { margin: 0; padding: 0; box-sizing: border-box; }
  html, body {
    width: 1200px; height: 801px; overflow: hidden;
    background: var(--backdrop);
    font-family: var(--font-main);
  }
  .stage {
    width: 1200px; height: 801px;
    display: flex; align-items: center; justify-content: center; gap: 60px;
  }
  .card {
    width: 525px; height: 300px; position: relative;
    box-shadow: 0 6px 18px rgba(0,0,0,0.25);
  }
  .card-front { background: var(--card-white); border-bottom: 3px solid var(--brand-teal); }
  .card-back { background: var(--brand-teal); display: flex; align-items: center; justify-content: center; }

  .brand-lockup {
    position: absolute; left: 42px; top: 50%; transform: translateY(-50%);
    display: flex; align-items: center; gap: 12px;
  }
  .brand-square { width: 22px; height: 22px; background: var(--brand-teal); border-radius: 4px; }
  .brand-name { font-weight: 500; font-size: 25px; color: var(--brand-teal); letter-spacing: 0.5px; }

  .divider {
    position: absolute; left: 300px; top: 62px; width: 1px; height: 176px;
    background: var(--brand-teal);
  }
  .contact-block {
    position: absolute; left: 318px; top: 52px;
    color: var(--text-grey); font-size: 11.5px; line-height: 1.45;
  }
  .person-name { font-weight: 700; font-size: 17px; color: var(--brand-teal); letter-spacing: 0.5px; }
  .person-title { margin-bottom: 16px; }
  .address { margin-bottom: 16px; }
  .contact-line { display: flex; align-items: center; gap: 7px; }
  .contact-line svg { width: 10px; height: 10px; flex: none; }

  .back-name { font-weight: 500; font-size: 28px; color: #3f8c82; letter-spacing: 0.5px; }
</style>
</head>
<body>
<main class="stage">
  <section class="card card-front" aria-label="Business card front">
    <div class="brand-lockup">
      <span class="brand-square"></span>
      <span class="brand-name">Corvana Group</span>
    </div>
    <div class="divider"></div>
    <div class="contact-block">
      <div class="person-name">MARLA QUINLAN</div>
      <div class="person-title">Co-Founder + CEO</div>
      <div class="address">1807 Harbor View Dr<br>Seacliff CA 90210</div>
      <div class="contact-line">
        <svg viewBox="0 0 10 10"><circle cx="5" cy="5" r="5" fill="var(--brand-teal)"/><path d="M3 3.2c.4 1.8 1.6 3 3.6 3.6" stroke="#fff" stroke-width="1.2" fill="none"/></svg>
        <span>555-014-2290</span>
      </div>
      <div class="contact-line">
        <svg viewBox="0 0 10 10"><rect x="0.5" y="2" width="9" height="6.5" rx="1" fill="var(--brand-teal)"/><path d="M1 2.5l4 3 4-3" stroke="#fff" stroke-width="0.9" fill="none"/></svg>
        <span>info@corvanagroup.com</span>
      </div>
      <div class="contact-line">
        <svg viewBox="0 0 10 10"><circle cx="5" cy="5" r="4.5" fill="var(--brand-teal)"/><path d="M0.5 5h9M5 0.5c-2 2.5-2 6.5 0 9M5 0.5c2 2.5 2 6.5 0 9" stroke="#fff" stroke-width="0.7" fill="none"/></svg>
        <span>www.corvanagroup.com</span>
      </div>
    </div>
  </section>

  <section class="card card-back" aria-label="Business card back">
    <span class="back-name">Corvana Group</span>
  </section>
</main>
</body>
</html>
```